Business Card Design Project

We require a business card template to cover basic contact information - our company logo, names of employees, title, mobile and email.

Target Market(s)

Corporate

Industry/Entity Type

Business

Font styles to use
Sans Serif

Requirements
Nice to have
• Thinking it would be great just to have the logo taking up approximately half the space (so it goes as far across the top of the card as possible) and then contact details in the lower half of the card. Keen just to use only the two colours in the logo, on a white background.
Should not have
• No fussy drawings

```html
<!DOCTYPE html>
<html lang="en">
<head>
<meta charset="utf-8">
<title>Tidewell developments – Business Card</title>
<link rel="stylesheet" href="https://fonts.googleapis.com/css2?family=Open+Sans:wght@400;600;700&display=swap">
<style>
  :root {
    --backdrop: #767676;
    --card: #ffffff;
    --blue-light: #3399cc;
    --blue-dark: #336699;
    --teal: #33a9bd;
    --white: #ffffff;
  }
  * { margin: 0; padding: 0; box-sizing: border-box; }
  html, body {
    width: 1200px;
    height: 1000px;
    overflow: hidden;
    background: var(--backdrop);
    font-family: "Open Sans", sans-serif;
  }
  .card {
    position: absolute;
    left: 129px;
    top: 195px;
    width: 940px;
    height: 605px;
    background: var(--card);
    overflow: hidden;
  }
  .brand {
    position: absolute;
    left: 0;
    top: 60px;
    width: 940px;
    color: var(--teal);
    font-weight: 600;
  }
  .brand-name {
    display: block;
    text-align: center;
    font-size: 176px;
    line-height: 1;
    letter-spacing: -4px;
  }
  .brand-tag {
    position: absolute;
    right: 110px;
    top: 178px;
    font-size: 46px;
    line-height: 1;
  }
  .bands {
    position: absolute;
    left: 0;
    top: 403px;
    width: 940px;
    height: 202px;
  }
  .person {
    position: absolute;
    left: 80px;
    top: 466px;
    width: 198px;
    text-align: center;
    color: var(--white);
  }
  .person-name {
    font-size: 32px;
    font-weight: 700;
    line-height: 1.1;
    white-space: nowrap;
  }
  .person-title {
    font-size: 23px;
    font-weight: 400;
    line-height: 1.2;
  }
  .contact {
    position: absolute;
    left: 552px;
    list-style: none;
    color: var(--white);
    font-size: 25px;
  }
  .contact li {
    display: flex;
    align-items: center;
    height: 44px;
    margin-bottom: 21px;
  }
  .contact-icon {
    width: 44px;
    height: 44px;
    margin-right: 16px;
    flex: none;
  }
  .contact { top: 449px; }
</style>
</head>
<body>
  <main class="card">
    <div class="brand">
      <span class="brand-name">Tidewell</span>
      <span class="brand-tag">developments</span>
    </div>

    <svg class="bands" viewBox="0 0 940 202" aria-hidden="true">
      <polygon points="0,0 546,0 526,22 0,22" fill="var(--blue-light)"/>
      <polygon points="566,0 940,0 940,22 546,22" fill="var(--blue-dark)"/>
      <rect x="0" y="36" width="940" height="130" fill="var(--blue-light)"/>
      <polygon points="0,178 519,178 539,202 0,202" fill="var(--blue-dark)"/>
      <polygon points="537,178 940,178 940,202 559,202" fill="var(--blue-light)"/>
    </svg>

    <div class="person">
      <p class="person-name">YOUR NAME</p>
      <p class="person-title">TITLE</p>
    </div>

    <ul class="contact">
      <li>
        <svg class="contact-icon" viewBox="0 0 44 44" aria-label="Phone">
          <circle cx="22" cy="22" r="21" fill="var(--white)"/>
          <path d="M11 18c0-4 5-6 11-6s11 2 11 6v2h-6v-3h-10v3h-6z" fill="var(--blue-dark)"/>
          <path d="M15 21h14l3 10H12z" fill="var(--blue-dark)"/>
          <circle cx="22" cy="26" r="3" fill="var(--white)"/>
        </svg>
        <span>+123 456 7890</span>
      </li>
      <li>
        <svg class="contact-icon" viewBox="0 0 44 44" aria-label="Email">
          <circle cx="22" cy="22" r="21" fill="var(--white)"/>
          <rect x="10" y="14" width="24" height="16" fill="var(--blue-dark)"/>
          <polyline points="10,14 22,24 34,14" fill="none" stroke="var(--white)" stroke-width="1.6"/>
          <polyline points="10,30 19,22 M34,30 25,22" fill="none" stroke="var(--white)" stroke-width="1.4"/>
        </svg>
        <span>yourname@mailbox.com</span>
      </li>
    </ul>
  </main>
</body>
</html>
```